Billboard Design for Equipment Rental Business

We need a billboard design for our equipment rental business called Brindlewood Equipment Company. We are based in Georgia. We rent construction tools, equipment, and dumpsters. We currently have a design but feel like we could get something better. Our phone number is 912-730-2591 and our website is www.brindlewoodequipment-example.com

```html
<!DOCTYPE html>
<html lang="en">
<head>
<meta charset="utf-8">
<title>Brindlewood Equipment Company — Billboard</title>
<link rel="stylesheet" href="https://fonts.googleapis.com/css2?family=Bebas+Neue&family=Montserrat:wght@600;700;800&display=swap">
<style>
  :root {
    --safety-yellow: #f8bf24;
    --art-yellow: #f6bb22;
    --art-yellow-deep: #eeb31f;
    --charcoal: #353333;
    --white: #ffffff;
    --backdrop: #97989a;
  }
  * { margin: 0; padding: 0; box-sizing: border-box; }
  html, body {
    width: 1152px;
    height: 1200px;
    overflow: hidden;
    background: var(--backdrop);
  }
  .billboard {
    position: absolute;
    left: 133px;
    top: 132px;
    width: 880px;
    height: 875px;
    overflow: hidden;
    background: var(--safety-yellow);
    font-family: "Montserrat", Arial, sans-serif;
    color: var(--charcoal);
    text-align: center;
  }
  .billboard__illustration {
    position: absolute;
    left: 253px;
    top: 19px;
    width: 433px;
    height: 309px;
  }
  .billboard__name,
  .billboard__descriptor,
  .billboard__phone,
  .billboard__web {
    position: absolute;
    left: 0;
    right: 0;
    line-height: 1;
    white-space: nowrap;
  }
  .billboard__name {
    top: 388px;
    font-weight: 800;
    font-size: 96px;
    letter-spacing: -1px;
  }
  .billboard__descriptor {
    top: 533px;
    font-weight: 700;
    font-size: 58px;
    letter-spacing: 0;
  }
  .billboard__band {
    position: absolute;
    left: 0;
    right: 0;
    top: 619px;
    height: 54px;
    background: var(--charcoal);
    color: var(--white);
    font-family: "Bebas Neue", Impact, sans-serif;
    font-size: 45px;
    line-height: 56px;
    letter-spacing: 0.1px;
    white-space: nowrap;
    overflow: hidden;
  }
  .billboard__phone {
    top: 697px;
    font-weight: 800;
    font-size: 94px;
    letter-spacing: 1px;
  }
  .billboard__web {
    top: 813px;
    font-weight: 700;
    font-size: 34px;
  }
</style>
</head>
<body>
  <main class="billboard">
    <svg class="billboard__illustration" role="img" aria-label="Line illustration of a tracked excavator with raised boom and bucket" viewBox="0 0 433 309">
      <defs>
        <linearGradient id="artTone" x1="0" y1="0" x2="0" y2="1">
          <stop offset="0" stop-color="#f6bb22"/>
          <stop offset="1" stop-color="#eeb31f"/>
        </linearGradient>
      </defs>
      <rect width="433" height="309" fill="url(#artTone)"/>
    </svg>

    <h1 class="billboard__name">BRINDLEWOOD</h1>
    <p class="billboard__descriptor">EQUIPMENT COMPANY</p>

    <p class="billboard__band">We rent construction tools, equipment, and dumpsters</p>

    <p class="billboard__phone">912-730-2591</p>
    <p class="billboard__web">www.brindlewoodequipment-example.com</p>
  </main>
</body>
</html>
```